Supply Chain Management Site - CrateLoomHQ

We are a supply chain management company that offers the following products:
Warehouse Management System (WMS)
Order Management System (OMS)
Delivery / Fleet Management System

Our product caters to 3PL and distributions.

Ideally a site with a light background would be good.
We like the following sites:
www.quintarel.com
http://www.bravelmo.com/us/
http://www.tirevka.com/

You can use the content from here:
http://host.sampleyard874.com/demo/crateloom-hq/

However, we really DO NOT like the design. You DO NOT have to have all the content on the home page. We can have the features and other things on other pages.

```html
<!DOCTYPE html>
<html lang="en">
<head>
<meta charset="utf-8">
<title>CrateLoom HQ – Agile, Dependable, Scalable</title>
<link href="https://fonts.googleapis.com/css2?family=Open+Sans:wght@400;600;700&family=Raleway:wght@400;500&display=swap" rel="stylesheet">
<style>
:root{
  --navy:#0a3f7e;
  --navy-deep:#08366c;
  --brand:#1d67c4;
  --button:#1a5fcc;
  --heading:#24517f;
  --text:#6b6b6b;
  --light:#f3f3f3;
  --footer:#2b2b2b;
  --footer-base:#1b1b1b;
  --footer-text:#9a9a9a;
  --white:#ffffff;
}
*{margin:0;padding:0;box-sizing:border-box}
html,body{width:1200px;height:900px;overflow:hidden;background:var(--white)}
body{font-family:"Open Sans",Arial,sans-serif;color:var(--text);position:relative}
.page{position:absolute;left:276px;top:0;width:648px;height:900px;background:var(--white)}
.abs{position:absolute}
.display{font-family:"Raleway","Open Sans",sans-serif;font-weight:400;color:var(--heading)}
/* top bar */
.topbar{left:0;top:0;width:648px;height:24px;background:var(--navy)}
.topbar .contact{left:104px;top:6px;font-size:6.5px;color:var(--white);display:flex;align-items:center;gap:4px}
.topbar .contact .gap{width:6px}
.social{display:flex;gap:2px}
.social span{width:9px;height:9px;border:1px solid rgba(255,255,255,.85)}
.topbar .social{left:474px;top:8px}
/* header */
.header{left:0;top:24px;width:648px;height:36px;background:var(--white)}
.logo{left:105px;top:3px;font-size:17px;color:var(--brand);font-family:"Open Sans",sans-serif;font-weight:400;line-height:20px}
.tagline{left:105px;top:23px;font-size:7.5px;color:var(--brand)}
.nav{left:337px;top:0;height:34px;display:flex}
.nav a{display:flex;flex-direction:column;align-items:center;justify-content:flex-end;padding:0 8px 6px;font-size:5px;color:#555;text-decoration:none;text-transform:uppercase;gap:5px}
.nav a.active{background:var(--navy);color:var(--white)}
.nav svg{width:8px;height:8px}
/* hero */
.hero{left:0;top:60px;width:648px;height:170px;background:var(--navy-deep)}
.hero-photo{left:81px;top:0;width:486px;height:170px;background:linear-gradient(100deg,#4b4137 0%,#7a5a3c 30%,#b99a75 55%,#d9d4c8 78%,#ece9e3 100%)}
.hero-copy{left:115px;top:49px;width:215px;color:var(--white)}
.hero-copy h1{font-size:10.5px;font-weight:700;line-height:13px}
.hero-copy h2{font-size:8px;font-weight:400;margin-top:1px}
.hero-copy p{font-size:4.6px;line-height:6.3px;margin-top:6px;color:#e8e8e8}
.btn-dark{left:115px;top:110px;width:58px;height:18px;background:#3e3a36;color:var(--white);font-size:4.8px;font-weight:700;display:flex;align-items:center;justify-content:center;letter-spacing:.3px}
/* sections */
.title{width:648px;text-align:center;font-size:14px}
.lead{width:452px;left:98px;text-align:center;font-size:5.3px;line-height:9.5px}
.btn-blue{left:300px;top:311px;width:48px;height:16px;background:var(--button);color:var(--white);font-size:4.3px;font-weight:700;display:flex;align-items:center;justify-content:center}
.product{top:370px;width:128px}
.product .photo{width:128px;height:56px}
.product h3{font-size:7.5px;font-weight:400;color:#555;text-align:center;margin-top:11px}
.product p{font-size:5.3px;line-height:9.3px;text-align:center;margin:6px auto 0;width:100px}
.tabs{left:263px;top:563px;display:flex;font-size:6px;font-weight:600;color:#333}
.tabs span{padding:2px 10px;border:1px solid transparent}
.tabs .on{background:var(--light);border-color:#e0e0e0}
.tabs .sep{width:1px;background:#ccc;padding:0;margin:2px 0}
.benefits-title{left:105px;top:579px;font-size:10px;font-weight:600;color:var(--heading)}
.benefits-intro{left:105px;top:600px;font-size:5.2px}
.benefits-body{left:105px;top:616px;width:258px;font-size:5.2px;line-height:9.2px}
.checks{left:105px;top:662px;list-style:none;font-size:5.2px}
.checks li{display:flex;align-items:center;gap:6px;height:12.4px}
.benefits-photo{left:369px;top:596px;width:165px;height:120px;background:radial-gradient(ellipse at 65% 45%,#d7c4b5 0%,#ece6e1 45%,#fafafa 75%)}
/* contact band */
.contact-band{left:0;top:722px;width:648px;height:58px;background:var(--navy)}
.ribbon{left:154px;top:715px;width:340px;height:15px;background:var(--brand);clip-path:polygon(4% 0,96% 0,100% 50%,96% 100%,4% 100%,0 50%);color:var(--white);font-family:"Raleway",sans-serif;font-size:9.5px;display:flex;align-items:center;justify-content:center;gap:4px}
.ribbon u{text-underline-offset:1px}
.contact-item{color:var(--white);display:flex;align-items:center;gap:8px}
.contact-item small{display:block;font-family:"Raleway",sans-serif;font-size:9.5px;line-height:11px}
.contact-item strong{display:block;font-size:12px;font-weight:700;line-height:15px}
/* footer */
.footer{left:0;top:780px;width:648px;height:92px;background:var(--footer)}
.footer h4{font-size:6.5px;font-weight:400;color:#ddd;text-transform:uppercase;letter-spacing:.3px}
.footer .tiny{font-size:4.3px;color:var(--footer-text);line-height:8px;text-transform:uppercase}
.rule{height:1px;background:#444}
.tweet{display:flex;gap:6px;font-size:4.3px;color:var(--footer-text)}
.newsletter-input{width:107px;height:12px;background:#1e1e1e;border:1px solid #3a3a3a}
.newsletter-send{width:25px;height:12px;background:#555;color:#ddd;font-size:4.5px;display:flex;align-items:center;justify-content:center}
.footer-base{left:0;top:872px;width:648px;height:28px;background:var(--footer-base)}
.footer-base .social{left:275px;top:10px;gap:4px}
.footer-base .social span{border:none;background:#cfcfcf;width:8px;height:8px}
</style>
</head>
<body>
<div class="page">

  <div class="abs topbar">
    <div class="abs contact">
      <svg width="6" height="9" viewBox="0 0 6 9"><rect x=".5" y=".5" width="5" height="8" rx="1" fill="none" stroke="#fff"/><circle cx="3" cy="7" r=".6" fill="#fff"/></svg>
      <span>(+01) 555 019 4820</span><span class="gap"></span>
      <svg width="9" height="7" viewBox="0 0 9 7"><rect x=".5" y=".5" width="8" height="6" fill="none" stroke="#fff"/><path d="M.5 .5 4.5 4 8.5 .5" fill="none" stroke="#fff"/></svg>
      <span>info@crateloomhq.com</span>
    </div>
    <div class="abs social"><span></span><span></span><span></span><span></span><span></span><span></span></div>
  </div>

  <header class="abs header">
    <div class="abs logo">CrateLoom HQ</div>
    <div class="abs tagline">Agile, Dependable, Scalable</div>
    <nav class="abs nav">
      <a class="active" href="#"><svg viewBox="0 0 8 8"><path d="M0 4 4 0 8 4H7V8H5V5H3V8H1V4Z" fill="#fff"/></svg>Home</a>
      <a href="#"><svg viewBox="0 0 8 8"><rect x="1" y="0" width="6" height="8" fill="#555"/></svg>About Us</a>
      <a href="#"><svg viewBox="0 0 8 8"><rect x="0" y="2" width="8" height="6" fill="#555"/><rect x="3" y="0" width="2" height="2" fill="#555"/></svg>Our Products</a>
      <a href="#"><svg viewBox="0 0 8 8"><rect x="1" y="0" width="6" height="8" rx="1" fill="#555"/></svg>Features</a>
      <a href="#"><svg viewBox="0 0 8 8"><path d="M0 3Q4 0 8 3V4H6V3H2V4H0Z M1 5H7V8H1Z" fill="#555"/></svg>Contact</a>
    </nav>
  </header>

  <section class="abs hero">
    <div class="abs hero-photo" role="img" aria-label="Warehouse aisle with tall pallet racking and forklift operators"></div>
    <div class="abs hero-copy">
      <h1>Northvane is your Business Solution</h1>
      <h2>Create Tablet marketing promotions in minutes</h2>
      <p>Lorem ipsum is simply dummy text of the printing and typesetting industry. Lorem ipsum has been the industry's standard, of type and scrambled it to make a type specimen book. It has survived into electronic typesetting.</p>
    </div>
    <div class="abs btn-dark">READ MORE</div>
  </section>

  <h2 class="abs title display" style="top:239px">Welcome To CrateLoom HQ</h2>
  <p class="abs lead" style="top:266px">Lorem ipsum dolor sit amet, consectetuer adipiscing elit. Aenean commodo ligula eget dolor. Aenean massa. Cum sociis natoque penatibus et magnis dis parturient montes, nascetur ridiculus mus. Donec quam felis, ultricies nec. Lorem ipsum dolor sit amet, consectetuer adipiscing elit. Aenean commodo ligula eget dolor. Aenean massa. Cum sociis natoque penatibus et magnis dis parturient montes, nascetur ridiculus mus. Donec quam felis, ultricies nec. Aenean massa. Cum sociis natoque penatibus et magnis dis parturient montes, nascetur ridiculus mus. Donec quam felis, ultricies nec.</p>
  <div class="abs btn-blue">KNOW MORE</div>

  <h2 class="abs title display" style="top:337px">We offers the following products</h2>

  <article class="abs product" style="left:104px">
    <div class="photo" role="img" aria-label="Warehouse worker with clipboard between stocked shelves" style="background:linear-gradient(90deg,#6b4a2e,#a07a55 50%,#5b4633)"></div>
    <h3>Warehouse Management System</h3>
    <p>Lorem ipsum dolor sit amet, consectetuer adipiscing elit. Aenean commodo ligula eget dolor. Aenean massa. Cum sociis.</p>
  </article>
  <article class="abs product" style="left:260px">
    <div class="photo" role="img" aria-label="Order flow diagram linking customer, phone, warehouse and delivery steps" style="background:linear-gradient(180deg,#9a9a9a,#7c7c7c)"></div>
    <h3>Order Management System</h3>
    <p>Lorem ipsum dolor sit amet, consectetuer adipiscing elit. Aenean commodo ligula eget dolor. Aenean massa. Cum sociis.</p>
  </article>
  <article class="abs product" style="left:417px">
    <div class="photo" role="img" aria-label="Delivery driver standing in front of a row of white trucks" style="background:linear-gradient(90deg,#e3e6ea,#c9ced4 55%,#b59f88)"></div>
    <h3>Delivery / Fleet Management System</h3>
    <p>Lorem ipsum dolor sit amet, consectetuer adipiscing elit. Aenean commodo ligula eget dolor. Aenean massa. Cum sociis.</p>
  </article>

  <h2 class="abs title display" style="top:499px">What a Warehouse Management System Should Be</h2>
  <p class="abs lead" style="top:525px;width:440px;left:104px">Lorem ipsum dolor sit amet, consectetuer adipiscing elit. Aenean commodo ligula eget dolor. Aenean massa. Cum sociis natoque penatibus et magnis dis parturient montes, nascetur ridiculus mus. Donec quam felis, ultricies nec. Lorem ipsum dolor sit amet, consectetuer adipiscing elit. Aenean commodo ligula eget dolor. Aenean massa. Cum sociis natoque penatibus et magnis dis parturient montes, nascetur ridiculus mus.</p>

  <div class="abs tabs"><span class="on">Major Benefits</span><span class="sep"></span><span>Key Features</span></div>

  <h3 class="abs benefits-title">Major Benefits</h3>
  <p class="abs benefits-intro">Lorem ipsum dolor sit amet, consectetur adipiscing elit</p>
  <p class="abs benefits-body">Lorem ipsum dolor sit amet, consectetur adipiscing elit, sed do eiusmod tempor incididunt ut labore et dolore magna aliqua. Ut enim ad minim veniam, quis nostrud exercitation ullamco laboris nisi ut aliquip ex ea commodo consequat. Duis aute irure dolor in reprehenderit in voluptate velit esse cillum dolore eu fugiat nulla pariatur. Excepteur sint occaecat cupidatat non proident, sunt in culpa qui officia deserunt mollit anim id est laborum.</p>
  <ul class="abs checks">
    <li><svg width="6" height="5" viewBox="0 0 6 5"><path d="M.5 2.5 2.2 4.2 5.5.6" fill="none" stroke="#24517f" stroke-width="1.3"/></svg>Vestibulum sapien nisl, ornare auctor, consectetuer quis, posuere tristique, odio.</li>
    <li><svg width="6" height="5" viewBox="0 0 6 5"><path d="M.5 2.5 2.2 4.2 5.5.6" fill="none" stroke="#24517f" stroke-width="1.3"/></svg>Duis volutpat elit et erat. In at nulla at nisl condimentum aliquet.</li>
    <li><svg width="6" height="5" viewBox="0 0 6 5"><path d="M.5 2.5 2.2 4.2 5.5.6" fill="none" stroke="#24517f" stroke-width="1.3"/></svg>Curabitur pretium tincidunt lacus. Nulla gravida orci a odio.</li>
    <li><svg width="6" height="5" viewBox="0 0 6 5"><path d="M.5 2.5 2.2 4.2 5.5.6" fill="none" stroke="#24517f" stroke-width="1.3"/></svg>Integer in mauris eu nibh euismod gravida.</li>
  </ul>
  <div class="abs benefits-photo" role="img" aria-label="Businessman sketching a light bulb idea with a marker"></div>

  <section class="abs contact-band">
    <div class="abs contact-item" style="left:122px;top:21px">
      <svg width="17" height="28" viewBox="0 0 17 28"><rect x="1" y="1" width="15" height="26" rx="2" fill="none" stroke="#fff" stroke-width="2"/><rect x="3.5" y="4" width="10" height="17" fill="#fff"/><circle cx="8.5" cy="24" r="1.2" fill="#fff"/></svg>
      <div><small>Customer Service</small><strong>(+03) 555 014 27 63</strong></div>
    </div>
    <div class="abs contact-item" style="left:377px;top:22px">
      <svg width="27" height="24" viewBox="0 0 27 24"><path d="M1 9 13.5 1 26 9V23H1Z" fill="none" stroke="#fff" stroke-width="2"/><path d="M1 9 13.5 17 26 9M1 23 10 15M26 23 17 15" fill="none" stroke="#fff" stroke-width="2"/></svg>
      <div><small>E- mail Us</small><strong>Infocrateloomhq.com</strong></div>
    </div>
  </section>
  <div class="abs ribbon">Need to know more about our product range <u>Get A Quote</u></div>

  <footer class="abs footer">
    <div class="abs" style="left:105px;top:15px;width:75px">
      <h4>Quick Link</h4>
      <p class="tiny" style="margin-top:9px">About Us &nbsp;|&nbsp; Products<br>Features &nbsp;|&nbsp; Contact</p>
      <div class="rule" style="margin:3px 0"></div>
      <p class="tiny">Copyright © 2015 CrateLoomHQ<br>All rights reserved</p>
    </div>
    <div class="abs" style="left:244px;top:15px;width:124px">
      <h4>Latest Tweet</h4>
      <div class="tweet" style="margin-top:9px"><span>●</span><span style="flex:1">" Featured products "<br><i>10 hours ago</i></span><span>DARA VELM</span></div>
      <div class="rule" style="margin:4px 0"></div>
      <div class="tweet"><span>●</span><span style="flex:1">" Visit the site "<br><i>11 hours ago</i></span><span>TOMAS REEL</span></div>
      <div class="rule" style="margin-top:4px"></div>
    </div>
    <div class="abs" style="left:413px;top:15px;width:135px">
      <h4>Newsletter</h4>
      <p class="tiny" style="margin-top:7px;text-transform:uppercase;font-style:italic">Sign up for our newsletter, and we'll keep you updated on all events at Quelvaro</p>
      <div style="display:flex;margin-top:8px"><div class="newsletter-input"></div><div class="newsletter-send">SEND</div></div>
    </div>
  </footer>
  <div class="abs footer-base">
    <div class="abs social"><span></span><span></span><span></span><span></span><span></span><span></span></div>
  </div>

</div>
</body>
</html>
```